K.D. Roofing LLC
President
K.D. Roofing LLC - Construction
Creative Brief
Professional
Mark Delvane III
4718 Falconer Ridge Lane Cherry Hill, NJ 08517
k.d.roofing.mdelvane@mailbox-example.com
I will be using gloss plastice business cards

```html
<!DOCTYPE html>
<html lang="en">
<head>
<meta charset="utf-8">
<title>K.D. Roofing LLC – Business Card</title>
<link href="https://fonts.googleapis.com/css2?family=PT+Sans:wght@400;700&family=Noto+Serif:ital,wght@1,700&display=swap" rel="stylesheet">
<style>
  :root {
    --page-bg: #e9e6e0;
    --card-bg: #f7f4ec;
    --green-dark: #4f9a17;
    --green: #6fb82a;
    --green-light: #a6d654;
    --grey-swoosh: #9a9a9a;
    --text: #2f2f2f;
    --text-muted: #6b6b6b;
  }
  * { margin: 0; padding: 0; box-sizing: border-box; }
  html, body {
    width: 1200px; height: 965px; overflow: hidden;
    background: var(--page-bg);
  }
  .canvas {
    position: relative; width: 1200px; height: 965px;
  }
  .card {
    position: absolute; left: 100px; top: 202px;
    width: 1000px; height: 560px;
    background: var(--card-bg);
    border-radius: 28px;
    overflow: hidden;
    box-shadow: 0 10px 30px rgba(0,0,0,0.18);
    font-family: "PT Sans", Arial, sans-serif;
    color: var(--text);
  }
  .card-bands { position: absolute; inset: 0; }
  .brand {
    position: absolute; left: 130px; top: 70px;
    display: flex; align-items: center; gap: 22px;
  }
  .brand-mark {
    width: 110px; height: 110px; border-radius: 50%;
    background: var(--green);
  }
  .brand-name {
    font-weight: 700; font-size: 50px; color: var(--green-dark);
    letter-spacing: 1px;
  }
  .address {
    position: absolute; left: 114px; top: 288px;
    font-size: 28px; line-height: 36px;
  }
  .contacts {
    position: absolute; left: 114px; top: 382px;
    list-style: none; font-size: 27px; line-height: 44px;
  }
  .contacts li { display: flex; align-items: center; gap: 12px; }
  .contact-icon { width: 24px; height: 24px; fill: var(--green-dark); flex: none; }
  .contact-at { width: 24px; text-align: center; color: var(--text); font-weight: 700; }
  .person {
    position: absolute; right: 80px; top: 392px; text-align: right;
    font-family: "Noto Serif", Georgia, serif; font-style: italic; font-weight: 700;
  }
  .person-name { font-size: 32px; color: var(--green-dark); }
  .person-title { font-size: 24px; color: var(--text-muted); margin-top: 2px; }
</style>
</head>
<body>
<main class="canvas">
  <section class="card">
    <svg class="card-bands" viewBox="0 0 1000 560" width="1000" height="560" aria-hidden="true">
      <defs>
        <linearGradient id="bandGreen" x1="0" y1="0" x2="1" y2="1">
          <stop offset="0" stop-color="#a6d654"/>
          <stop offset="0.55" stop-color="#6fb82a"/>
          <stop offset="1" stop-color="#4f9a17"/>
        </linearGradient>
      </defs>
      <path d="M0 0 H70 C20 150 15 380 55 560 H0 Z" fill="url(#bandGreen)"/>
      <path d="M78 0 C30 150 28 380 70 560" fill="none" stroke="#9a9a9a" stroke-width="9"/>
      <path d="M800 0 H1000 V450 C985 250 930 90 800 0 Z" fill="url(#bandGreen)"/>
      <path d="M770 0 C905 80 965 240 985 460" fill="none" stroke="#9a9a9a" stroke-width="9"/>
    </svg>

    <header class="brand">
      <div class="brand-mark"></div>
      <div class="brand-name">K.D. Roofing LLC</div>
    </header>

    <address class="address" style="font-style:normal">
      4718 Falconer Ridge Lane<br>
      Cherry Hill, NJ 08517
    </address>

    <ul class="contacts">
      <li>
        <svg class="contact-icon" viewBox="0 0 24 24" aria-hidden="true"><path d="M6.6 10.8a15 15 0 0 0 6.6 6.6l2.2-2.2a1 1 0 0 1 1-.25 11.4 11.4 0 0 0 3.6.57 1 1 0 0 1 1 1V20a1 1 0 0 1-1 1A17 17 0 0 1 3 4a1 1 0 0 1 1-1h3.5a1 1 0 0 1 1 1c0 1.25.2 2.45.57 3.6a1 1 0 0 1-.25 1z"/></svg>
        856-555-0142
      </li>
      <li>
        <svg class="contact-icon" viewBox="0 0 24 24" aria-hidden="true"><path d="M7 1h10a2 2 0 0 1 2 2v18a2 2 0 0 1-2 2H7a2 2 0 0 1-2-2V3a2 2 0 0 1 2-2zm0 3v14h10V4zm5 15.5a1 1 0 1 0 0 2 1 1 0 0 0 0-2z"/></svg>
        856-555-0179
      </li>
      <li>
        <span class="contact-at">@</span>
        k.d.roofing.mdelvane@mailbox-example.com
      </li>
    </ul>

    <div class="person">
      <div class="person-name">Mark Delvane III</div>
      <div class="person-title">President</div>
    </div>
  </section>
</main>
</body>
</html>
```